Quillmera

Business cards and core flute signage. The business is only in its infant as a 'market' business. I would like the name to be curved across the page in different colours with a bold line underneath finished with an exotic pen drawing the line. (Similar to pictures)
We are trying to reach all markets as they are designer pens and items are made as requested or they can select from already manufactured pens on display.
I have included some images of the actual pens that I make for inspiration, we are very open to your ideas and guidance if you have a specific design in mind.
If you would more pen photo options, please contact me with your email details.
Darren Talbiro
Pen Maker & Wood Turner
Ph. 0438 271 546
Target Market(s)
Generally professional customers who would use a pen for work on a daily basis
Industry/Entity Type
Business
Requirements
Must have
- Punchy and catchy styling
Nice to have
- One of my pens

```html
<!DOCTYPE html>
<html lang="en">
<head>
<meta charset="utf-8">
<title>Quillmera – business card options</title>
<link rel="stylesheet" href="https://fonts.googleapis.com/css2?family=Arimo:wght@400;700&family=Yesteryear&display=swap">
<style>
  :root {
    --page: #ffffff;
    --label: #333333;
    --gold-light: #f3c25a;
    --gold: #c9892a;
    --rust: #7a3d12;
    --rust-deep: #4a230a;
    --band: #1e1b18;
    --band-edge: #e0a63c;
    --wordmark: #f0a53a;
    --ink: #1f160e;
    --pen-copper: #b35a22;
    --pen-black: #222226;
    --pen-white: #e9e6e0;
    --pen-silver: #9a9690;
  }
  * { box-sizing: border-box; margin: 0; padding: 0; }
  html, body { width: 1001px; height: 1200px; overflow: hidden; background: var(--page); }
  .sheet { position: relative; width: 1001px; height: 1200px; }
  .option-label {
    position: absolute; left: 38px; font: 400 38px/1 Arimo, sans-serif; color: var(--label);
  }
  .option-label--one { top: 296px; }
  .option-label--two { top: 864px; }

  .card {
    position: absolute; left: 92px; width: 853px; height: 503px; overflow: hidden;
  }
  .card--one { top: 74px; }
  .card--two { top: 627px; }

  .card__texture {
    position: absolute; inset: 0;
    background:
      radial-gradient(ellipse 45% 40% at 35% 72%, var(--gold-light) 0%, rgba(243,194,90,0) 100%),
      radial-gradient(ellipse 60% 30% at 40% 8%, var(--gold) 0%, rgba(201,137,42,0) 100%),
      linear-gradient(180deg, var(--rust) 0%, var(--gold) 45%, var(--rust) 100%);
  }
  .card__band { position: absolute; left: 0; top: 0; width: 853px; height: 503px; }
  .card__pens { position: absolute; left: 0; top: 0; width: 853px; height: 503px; }

  .wordmark {
    position: absolute; left: 69px; top: 128px;
    font: 700 66px/1 Arimo, sans-serif; color: var(--wordmark);
  }
  .tagline {
    position: absolute; left: 128px; top: 262px;
    font: 400 50px/1 Yesteryear, cursive; color: var(--ink);
  }
  .contact { position: absolute; right: 250px; top: 352px; text-align: right; color: var(--ink); }
  .contact__name { font: 700 22px/1.2 Arimo, sans-serif; }
  .contact__role { font: 400 23px/1.5 Yesteryear, cursive; }
  .contact__role--plain { font: 400 19px/1.7 Arimo, sans-serif; }
  .contact__phone { font: 400 21px/1.5 Arimo, sans-serif; display: flex; align-items: center; justify-content: flex-end; gap: 3px; }
  .contact__phone svg { width: 16px; height: 18px; }
</style>
</head>
<body>
<main class="sheet">
  <span class="option-label option-label--one">1</span>
  <span class="option-label option-label--two">2</span>

  <section class="card card--one">
    <div class="card__texture" role="img" aria-label="Burnished gold and rust textured background"></div>
    <svg class="card__band" viewBox="0 0 853 503" aria-hidden="true">
      <path d="M0 112 L120 108 L260 100 L420 82 L490 90 L560 100 L853 96 L853 220 L640 226 L480 240 L300 228 L150 236 L0 230 Z" fill="var(--band)"/>
      <path d="M0 112 L120 108 L260 100 L420 82 L490 90 L560 100" fill="none" stroke="var(--band-edge)" stroke-width="2"/>
    </svg>
    <svg class="card__pens" viewBox="0 0 853 503" role="img" aria-label="Three handmade pens laid diagonally: copper acrylic, black and white marbled, and white with an ornate cap">
      <defs>
        <linearGradient id="pens-one" x1="0" y1="0" x2="1" y2="0">
          <stop offset="0" stop-color="var(--pen-copper)"/>
          <stop offset="0.4" stop-color="var(--pen-black)"/>
          <stop offset="0.7" stop-color="var(--pen-white)"/>
          <stop offset="1" stop-color="var(--pen-silver)"/>
        </linearGradient>
      </defs>
      <path d="M491 111 L575 0 L700 0 L853 380 L853 503 L800 503 Z" fill="url(#pens-one)"/>
    </svg>
    <div class="wordmark">Quillmera</div>
    <div class="tagline">custom handmade pens</div>
    <div class="contact">
      <p class="contact__name">Darren Talbiro</p>
      <p class="contact__role">Pen Maker and Wood Turner</p>
      <p class="contact__phone"><svg viewBox="0 0 16 18" aria-hidden="true"><path d="M4 1 L7 5 L5 7 Q6 11 10 13 L12 11 L15 14 L13 17 Q3 15 1 4 Z" fill="var(--ink)"/></svg>0438 271 546</p>
    </div>
  </section>

  <section class="card card--two">
    <div class="card__texture" role="img" aria-label="Burnished gold and rust textured background"></div>
    <svg class="card__band" viewBox="0 0 853 503" aria-hidden="true">
      <path d="M0 112 L120 108 L260 100 L420 82 L490 90 L560 100 L853 96 L853 220 L640 226 L480 240 L300 228 L150 236 L0 230 Z" fill="var(--band)"/>
      <path d="M0 112 L120 108 L260 100 L420 82 L490 90 L560 100" fill="none" stroke="var(--band-edge)" stroke-width="2"/>
    </svg>
    <svg class="card__pens" viewBox="0 0 853 503" role="img" aria-label="Three handmade pens laid diagonally: copper acrylic, black and white marbled, and white with an ornate cap">
      <defs>
        <linearGradient id="pens-two" x1="0" y1="0" x2="1" y2="0">
          <stop offset="0" stop-color="var(--pen-copper)"/>
          <stop offset="0.4" stop-color="var(--pen-black)"/>
          <stop offset="0.7" stop-color="var(--pen-white)"/>
          <stop offset="1" stop-color="var(--pen-silver)"/>
        </linearGradient>
      </defs>
      <path d="M491 111 L575 0 L700 0 L853 380 L853 503 L800 503 Z" fill="url(#pens-two)"/>
    </svg>
    <div class="wordmark">Quillmera</div>
    <div class="tagline">custom handmade pens</div>
    <div class="contact">
      <p class="contact__name">Darren Talbiro</p>
      <p class="contact__role contact__role--plain">Pen Maker and Wood Turner</p>
      <p class="contact__phone"><svg viewBox="0 0 16 18" aria-hidden="true"><path d="M4 1 L7 5 L5 7 Q6 11 10 13 L12 11 L15 14 L13 17 Q3 15 1 4 Z" fill="var(--ink)"/></svg>0438 271 546</p>
    </div>
  </section>
</main>
</body>
</html>
```